Letterhead design for Sleep Consulting Business

I'm looking for a new letterhead (heading/footer) design for my Sleep Consulting Business, I work with families to help their children improve their sleep.

The heading/footer will used in Microsoft Word Only-to be used for all of my documents such as writing Sleep Plans. I need to utilize as much working space in the document as possible. This will NOT be printed out on paper- it will only be used for heading/footer on microsoft word, then emailed to clients, who may print it at home.

My brand colors:
Dark Blue Hex: 1F2A42
Lighter Blueish Hex: 90BEC9
You're welcome to check out my website for inspiration- it is freshly created with other colors as well, and I love the outcome. www.quietharborsleep.example

Target Market(s)

Tired parents

Font styles to use
Script
Other font styles liked:
• Great Vibe, Lato or Just Another Hand are all used currently for my brand. Open to other options.

Requirements
Must have
• The letterhead (heading/footer) MUST be kept narrow (height-wise), so I have plenty of space on my document, while including important information.

It should look professional on screen, and when printed.

Must include my business name OR logo (Quiet Harbor Sleep Consulting), and my email address. Tessa@quietharborsleep.example

Website is optional, not required, just if you need to fill in a spot: www.quietharborsleep.example

```html
<!DOCTYPE html>
<html lang="en">
<head>
<meta charset="utf-8">
<title>Quiet Harbor Sleep Consulting — Letterhead</title>
<link rel="stylesheet" href="https://fonts.googleapis.com/css2?family=Arimo:wght@400&family=Lato:wght@400;700&display=swap">
<style>
  :root {
    --navy: #1F2A42;
    --mist: #90BEC9;
    --paper: #ffffff;
    --backdrop: #e4eef0;
    --ink: #1c1c1c;
  }
  * { margin: 0; padding: 0; box-sizing: border-box; }
  html, body { width: 1200px; height: 1200px; overflow: hidden; background: var(--backdrop); }
  .letterhead {
    position: absolute; left: 176px; top: 0;
    width: 848px; height: 1200px;
    background: var(--paper); overflow: hidden;
  }
  .letterhead-art { position: absolute; inset: 0; width: 100%; height: 100%; }
  .brand {
    position: absolute; left: 88px; top: 76px;
    display: flex; align-items: center; gap: 18px;
  }
  .brand-dot { width: 98px; height: 98px; border-radius: 50%; background: var(--mist); flex: none; }
  .brand-name {
    font-family: "Lato", sans-serif; font-weight: 400;
    font-size: 23px; letter-spacing: 0.5px; color: var(--navy); white-space: nowrap;
  }
  .contact {
    position: absolute; left: 560px; top: 139px;
    font-family: "Lato", sans-serif; font-weight: 700; font-size: 12.5px; color: var(--navy);
    list-style: none;
  }
  .contact li { display: flex; align-items: center; gap: 6px; height: 18px; }
  .contact svg { width: 13px; height: 13px; flex: none; }
  .letter-body {
    position: absolute; left: 90px; top: 333px; width: 690px;
    font-family: "Arimo", Arial, sans-serif; font-size: 15.6px; line-height: 27px; color: var(--ink);
  }
  .letter-body p + p { margin-top: 9px; }
  .signature { position: absolute; left: 90px; top: 902px; }
  .signature-mark { width: 112px; height: 56px; background: #e3f1f8; border-radius: 4px; }
  .signature-label { font-family: "Arimo", Arial, sans-serif; font-size: 10px; color: var(--ink); margin-top: 6px; }
</style>
</head>
<body>
  <main class="letterhead">
    <svg class="letterhead-art" viewBox="0 0 852 1205" preserveAspectRatio="none" aria-hidden="true">
      <path class="header-swoosh" fill="var(--mist)" d="M525 0 L852 0 L852 205 C835 120 740 60 640 30 C600 15 560 5 525 0 Z"/>
      <path class="header-wave" fill="var(--navy)" d="M525 0 L852 0 L852 145 C790 85 720 50 660 32 C610 15 560 5 525 0 Z"/>
      <rect class="header-rule" x="0" y="205" width="852" height="8" fill="var(--navy)"/>
      <path class="footer-swoosh" fill="var(--mist)" d="M550 1158 C700 1152 800 1120 852 1085 L852 1192 C750 1188 650 1172 550 1160 Z"/>
      <path class="footer-wave" fill="var(--navy)" d="M0 1000 C200 1090 400 1148 560 1167 C680 1182 780 1195 852 1199 L852 1205 L0 1205 Z"/>
    </svg>

    <header>
      <div class="brand">
        <span class="brand-dot"></span>
        <span class="brand-name">Quiet Harbor Sleep Consulting</span>
      </div>
      <ul class="contact">
        <li>
          <svg viewBox="0 0 14 14"><rect x="1" y="3" width="12" height="8" fill="var(--mist)"/><path d="M1 3 L7 8 L13 3" fill="none" stroke="#fff" stroke-width="1.2"/></svg>
          www.quietharborsleep.example
        </li>
        <li>
          <svg viewBox="0 0 14 14"><circle cx="7" cy="7" r="6" fill="var(--mist)"/><path d="M1 7 H13 M7 1 C3 5 3 9 7 13 M7 1 C11 5 11 9 7 13" fill="none" stroke="#fff" stroke-width="1"/></svg>
          Tessa@quietharborsleep.example
        </li>
      </ul>
    </header>

    <section class="letter-body">
      <p>Lorem ipsum dolor sit amet, consectetur adipiscing elit. Maecenas at dapibus diam. Vivamus fringilla nulla lorem, sit amet mollis nisi suscipit in. Donec lacus tortor, finibus eget pharetra vitae, auctor eget augue. Mauris euismod libero ac risus fermentum, sed rhoncus erat consectetur. Phasellus eget hendrerit ligula, id volutpat tellus. Praesent viverra sapien at convallis eleifend. Pellentesque ac ipsum felis. Vestibulum augue massa, blandit eu tellus eu, fringilla volutpat quam.</p>
      <p>Nulla in neque sit amet diam lobortis lacinia. Donec tristique tristique ex in fermentum. Donec tristique erat non turpis sollicitudin, et posuere dui congue. Nulla elementum finibus orci, in varius ligula feugiat ut. Donec viverra hendrerit est, quis pulvinar metus pretium et. Lorem ipsum dolor sit amet, consectetur adipiscing elit. Nulla tempus pretium convallis. Nunc imperdiet tempus sem sit amet rutrum. Morbi tempus in lacus sed sollicitudin. Praesent non sem commodo, faucibus metus id, imperdiet odio. Morbi sodales convallis nulla a rutrum. Class aptent taciti sociosqu ad litora torquent per conubia nostra, per inceptos himenaeos. Nulla condimentum iaculis tellus non scelerisque. Fusce lobortis gravida pretium.</p>
      <p>Cras nec quam mauris. Nulla eu urna eu tortor bibendum eleifend. Nulla imperdiet semper ex, ac iaculis massa consequat eget. Maecenas quis dui varius, tincidunt massa vitae, condimentum lacus. Aliquam in viverra lorem. Integer eros tortor, tristique ac quam in, tempor accumsan lectus. Nulla in neque tellus.</p>
    </section>

    <footer class="signature">
      <div class="signature-mark" role="img" aria-label="Handwritten signature in light blue ink"></div>
      <div class="signature-label">Signature</div>
    </footer>
  </main>
</body>
</html>
```